LAW FIRM - RE-DESIGN - (professional, excellence, tradition and innovation)

We are a premier law firm in New South Wales, Australia. We pride ourselves on being cutting edge and up to date in our market.

Our firm formed in 1874 and has a particularly strong tradition within it's geographic footprint. acting for clients over multiple generations. Despite our regional background, our reputation for excellence has enable us to remain highly visible in a large area.

We have invested heavily in ensuring future planning of this business, and do so on a recurring basis. This has lead to a review of our existing web site.

Although serviceable we feel our previous website is out-of-date and not as in touch with the modern market. We are aware that for the emerging clients a web site is often the face of a firm and a failure to hold attention on the first page may fail to capture the client.

We are seeking designs to communicate the core values of professionalism and excellence. At the same time as maintaining traditional country values of honesty, integrity and hard work we strive to embrace changes to the law and technology.

Target Market(s)

Clients of Law Firm

Industry/Entity Type

Law Firm

Coding

Coded - Design and coding required

Number of Pages Required

5+ page

Requirements
Must have
• A strong sense of professionalism and excellence with a careful balance between traditional values and innovation.
Nice to have
• We have included within our design brief links to top competitors sites to assist for design concepts.

```html
<!DOCTYPE html>
<html lang="en">
<head>
<meta charset="utf-8">
<title>Hartwell Law</title>
<link href="https://fonts.googleapis.com/css2?family=Lato:ital,wght@0,400;0,700;1,400&family=Ubuntu:wght@400;500&family=Libre+Baskerville:wght@700&display=swap" rel="stylesheet">
<style>
:root{
  --navy:#0b3468;
  --navy-deep:#082a55;
  --navy-mid:#1a4a82;
  --sky:#4aa3df;
  --white:#ffffff;
  --ink:#333a44;
  --grey-bg:#f1f1f1;
  --footer-bar:#0a2f5e;
}
*{margin:0;padding:0;box-sizing:border-box}
html,body{width:1200px;height:3220px;overflow:hidden}
body{position:relative;font-family:"Lato",sans-serif;color:var(--ink);background:var(--white)}
.abs{position:absolute}
a{color:inherit;text-decoration:none}

/* header */
.site-header{left:0;top:0;width:1200px;height:135px;background:var(--white)}
.brand{left:78px;top:30px;font-family:"Ubuntu",sans-serif;font-weight:500;font-size:38px;color:var(--navy);letter-spacing:1px;display:flex;align-items:center;gap:10px}
.brand-dot{width:14px;height:14px;background:var(--navy);border-radius:50%}
.social-top{right:78px;top:12px;display:flex;gap:9px}
.social-top span{width:38px;height:38px;border-radius:50%;background:var(--navy)}
.social-top span:nth-child(n+2){background:#8c8c8c}
.main-nav{right:78px;top:78px;display:flex;gap:42px;font-size:17px;letter-spacing:.5px;color:#3a4658}
.main-nav .active{color:var(--navy);font-weight:700}
.caret{display:inline-block;width:0;height:0;border-left:6px solid transparent;border-right:6px solid transparent;border-top:7px solid currentColor;margin-left:8px;vertical-align:2px}

/* hero */
.hero{left:0;top:135px;width:1200px;height:575px;background:linear-gradient(90deg,#3a2a22 0%,#5b4536 30%,#3b3a4e 55%,#5a2a30 80%,#2b2228 100%)}
.hero-person{right:0;top:0;width:330px;height:575px;background:linear-gradient(180deg,#6a5a58,#1f1a1d)}
.hero-title{left:0;top:140px;width:1200px;text-align:center;font-family:"Libre Baskerville",serif;font-size:66px;color:var(--white);letter-spacing:2px}
.hero-sub{left:0;top:225px;width:1200px;text-align:center;font-size:19px;line-height:1.4;color:var(--white)}
.btn-outline{border:2px solid rgba(255,255,255,.85);color:var(--white);font-size:17px;text-align:center;letter-spacing:.5px}
.hero-btn{left:508px;top:305px;width:184px;height:55px;line-height:51px}

/* about */
.about{left:0;top:710px;width:1200px;height:365px;background:var(--navy)}
.section-title{font-family:"Ubuntu",sans-serif;font-weight:400;color:var(--white);font-size:42px}
.about .section-title{left:0;top:46px;width:1200px;text-align:center}
.about-text{left:190px;top:108px;width:820px;text-align:center;font-size:13.5px;line-height:1.45;color:#dfe6f0}
.about-text p+p{margin-top:16px}
.about-btn{left:522px;top:262px;width:156px;height:48px;line-height:44px}

/* philosophy */
.philosophy{left:0;top:1075px;width:1200px;height:310px;background:linear-gradient(90deg,#d8dbe0,#f4f5f7 40%,#e2e4e8)}
.philosophy-photo{left:0;top:0;width:618px;height:310px;background:linear-gradient(135deg,#5a3a2c,#2b2a2e 55%,#7a6a60);clip-path:polygon(0 0,100% 0,92% 100%,0 100%)}
.philosophy .section-title{left:628px;top:30px;color:var(--navy);font-size:40px}
.philosophy-text{left:628px;top:92px;width:500px;font-size:13.5px;line-height:1.42;color:#2b2f36}
.philosophy-text .quote{font-style:italic}
.philosophy-text p+p{margin-top:10px}

/* services */
.services{left:0;top:1385px;width:1200px;height:645px;background:linear-gradient(180deg,#21497d,#143e73 60%,#1b4880)}
.services .section-title{left:78px;top:50px;font-size:40px}
.services-intro{left:78px;top:110px;width:1045px;font-size:13.5px;line-height:1.4;color:#e3eaf3}
.expertise-title{left:78px;top:222px;font-family:"Ubuntu",sans-serif;font-size:26px;color:var(--white)}
.expertise-list{top:275px;list-style:none;font-size:15px;color:#e6edf5}
.expertise-list li{height:31.3px;display:flex;align-items:center}
.expertise-list li::before{content:"";width:8px;height:8px;border-radius:50%;background:var(--sky);margin-right:15px}
.list-a{left:78px}
.list-b{left:338px}
.tile{width:186px;height:142px;border:2px solid #c9d3e0}
.tile-a{left:735px;top:280px;background:linear-gradient(135deg,#cfd6de,#7e8893)}
.tile-b{left:937px;top:280px;background:#2c2f35;border-color:#3a3e46;color:var(--white);font-size:19px;letter-spacing:1px;display:flex;align-items:center;justify-content:center}
.tile-c{left:735px;top:447px;background:linear-gradient(135deg,#e6eaf0,#5c7fa8)}
.tile-d{left:937px;top:447px;background:linear-gradient(135deg,#b7b9bd,#3b3535)}
.slider-arrow{width:25px;height:25px;background:var(--white);border:1px solid #9aa;display:flex;align-items:center;justify-content:center;top:312px}

/* people */
.people{left:0;top:2030px;width:1200px;height:460px;background:var(--grey-bg)}
.people .section-title{left:0;top:42px;width:1200px;text-align:center;color:#3d4552;font-size:42px}
.person{top:128px;width:140px;text-align:center}
.person-photo{width:126px;height:164px;margin:0 auto;border:4px solid var(--white);outline:1px solid #9aa3ad;background:linear-gradient(180deg,#a58a66,#6b5a48 45%,#2a2c33)}
.person-name{margin-top:22px;font-size:16px;color:#3d4552}
.btn-navy{border:2px solid var(--navy);color:var(--navy);font-size:15px;text-align:center}
.people-btn{left:522px;top:358px;width:156px;height:48px;line-height:44px}

/* contact */
.contact{left:0;top:2490px;width:1200px;height:385px;background:linear-gradient(90deg,#2a2c30,#3d3f44 50%,#26282c)}
.contact .section-title{left:0;top:42px;width:1200px;text-align:center;font-size:42px}
.field{border:2px solid rgba(255,255,255,.75);color:var(--white);font-size:15px;padding:8px 16px}
.f-name{left:233px;top:113px;width:312px;height:45px}
.f-phone{left:233px;top:161px;width:312px;height:45px}
.f-mail{left:233px;top:209px;width:312px;height:45px}
.f-msg{left:552px;top:113px;width:415px;height:141px}
.submit{left:528px;top:275px;width:144px;height:50px;line-height:46px;background:var(--navy);border:2px solid #c9d3e0;color:var(--white);font-size:16px;text-align:center;letter-spacing:.5px}

/* footer */
.site-footer{left:0;top:2875px;width:1200px;height:290px;background:var(--white)}
.footer-title{left:78px;top:30px;font-family:"Ubuntu",sans-serif;font-size:25px;color:#2b2f36}
.office{top:80px;width:260px;font-size:13.5px;color:#4a4f58}
.office-head{display:flex;gap:14px}
.office-name{font-weight:700;color:var(--navy);font-size:14px;margin-bottom:5px}
.office-line{display:flex;align-items:center;gap:16px;margin-top:16px}
.office-line svg{flex:none}
.office-note{font-style:italic;margin-left:42px;margin-top:4px}
.footer-brand{left:940px;top:68px;font-family:"Ubuntu",sans-serif;font-weight:500;font-size:34px;color:var(--navy);display:flex;align-items:center;gap:10px}
.footer-social{left:927px;top:190px;display:flex;gap:12px}
.footer-social span{width:46px;height:46px;border-radius:50%;background:var(--navy)}
.footer-social span:nth-child(n+2){background:var(--white);border:2px solid var(--navy)}
.copyright{left:0;top:3165px;width:1200px;height:55px;background:var(--footer-bar);color:var(--white);font-size:14px;text-align:center;line-height:55px}
</style>
</head>
<body>

<header class="site-header abs">
  <div class="brand abs"><span class="brand-dot"></span>Hartwell Law</div>
  <div class="social-top abs"><span></span><span></span><span></span><span></span></div>
  <nav class="main-nav abs">
    <a class="active">ABOUT<i class="caret"></i></a>
    <a>SERVICES<i class="caret"></i></a>
    <a>PEOPLE<i class="caret"></i></a>
    <a>COMMUNITY</a>
    <a>CONTACT US</a>
  </nav>
</header>

<section class="hero abs" role="img" aria-label="Courtroom scene with a scale of justice statue and a flag behind">
  <div class="hero-person abs" role="img" aria-label="Smiling lawyer in a robe holding a red law book"></div>
  <h1 class="hero-title abs">HARTWELL LAW</h1>
  <p class="hero-sub abs">Hartwell law is a legal firm geographically based within the High Country<br>region of New South Wales, Australia.</p>
  <a class="hero-btn btn-outline abs">CONTACT US</a>
</section>

<section class="about abs">
  <h2 class="section-title abs">About Hartwell Law</h2>
  <div class="about-text abs">
    <p>Hartwell Law has been in existence since 1874 originally starting out as the firm Edwin Cartwright of Kingsford Ridge. In 1894 Edwin Cartwright was acquired by Colonel RJ Whitlock. The firm became known as RJ Whitlock &amp; Co. until early 1970 when it became Whitlock &amp; Co, Whitlock Hale &amp; Co in 1979 and Whitlock Hale &amp; Morrow in 1982.</p>
    <p>In December 1999, the firm opened an office in Marlow Downs taking over the practice of LM Fenwick &amp; Associates. This was followed by the incorporation of Ashcombe &amp; Co in December 2000 and the Bellbrook office moved to larger premises in Wattle Street.</p>
  </div>
  <a class="about-btn btn-outline abs">READ MORE</a>
</section>

<section class="philosophy abs">
  <div class="philosophy-photo abs" role="img" aria-label="Lawyers meeting around a desk in an office"></div>
  <h2 class="section-title abs">Our Philosophy</h2>
  <div class="philosophy-text abs">
    <p class="quote">" Driven by quality legal work and service, Hartwell Law is founded on and values integrity, honesty, personal excellence, mutual respect and commitment to team work."</p>
    <p>Hartwell Law is built on strength, independence, integrity and an enthusiasm for the law. Our 'down to earth' culture stems from the firms country origins and close ties to the communities in which it operates.</p>
    <p>We value an open and honest approach to all client service, ensuring the highest level of communication with clients and the Hartwell Law team.</p>
  </div>
</section>

<section class="services abs">
  <h2 class="section-title abs">Our Services</h2>
  <p class="services-intro abs">We value an open and honest approach to all client service, ensuring the highest level of communication with clients and the Hartwell Law team. Succession planning allows for the orderly maintenance of property and small businesses ownership. Since that time Hartwell Law has maintained a dominant presence. Additionally, although this firm has its genesis within the High Country region, we service client's well outside our geographic footprint including capital cities and abroad. In an exceptionally competitive market, we attribute our success to uncompromising professionalism and excellence in the work undertaken.</p>
  <h3 class="expertise-title abs">Our areas of expertise include:</h3>
  <ul class="expertise-list list-a abs">
    <li>Building &amp; Construction</li><li>Corporate &amp; Commercial</li><li>Criminal Law</li><li>Employment</li><li>Family Law</li><li>Environmental</li><li>Insurance</li><li>Intellectual Property</li><li>Powers of Attorney</li><li>Succession Planning</li>
  </ul>
  <ul class="expertise-list list-b abs">
    <li>Estate Administration &amp; Probate</li><li>Enduring Guardianship Agreements</li><li>Litigation &amp; Dispute Resolution</li><li>Occupational Health &amp; Safety</li><li>Property (including Leasing and Conveyancing)</li><li>Trade Practices</li><li>Transport</li><li>Water Rights</li><li>Wills</li>
  </ul>
  <div class="tile tile-a abs" role="img" aria-label="Lawyer and client reviewing documents"></div>
  <div class="tile tile-b abs">READ MORE</div>
  <div class="tile tile-c abs" role="img" aria-label="Business handshake"></div>
  <div class="tile tile-d abs" role="img" aria-label="Barristers in robes carrying files"></div>
  <div class="slider-arrow abs" style="left:36px"><svg width="10" height="12" viewBox="0 0 10 12"><path d="M7 1 2 6l5 5" fill="none" stroke="#333" stroke-width="2"/></svg></div>
  <div class="slider-arrow abs" style="left:1140px"><svg width="10" height="12" viewBox="0 0 10 12"><path d="M3 1l5 5-5 5" fill="none" stroke="#333" stroke-width="2"/></svg></div>
</section>

<section class="people abs">
  <h2 class="section-title abs">People</h2>
  <div class="person abs" style="left:71px"><div class="person-photo" role="img" aria-label="Portrait of Daniel Okafor"></div><p class="person-name">Daniel Okafor</p></div>
  <div class="person abs" style="left:303px"><div class="person-photo" role="img" aria-label="Portrait of Helen Moray"></div><p class="person-name">Helen Moray</p></div>
  <div class="person abs" style="left:530px"><div class="person-photo" role="img" aria-label="Portrait of Graham Hale"></div><p class="person-name">Graham Hale</p></div>
  <div class="person abs" style="left:745px"><div class="person-photo" role="img" aria-label="Portrait of Julia Brent"></div><p class="person-name">Julia Brent</p></div>
  <div class="person abs" style="left:990px"><div class="person-photo" role="img" aria-label="Portrait of Ross Morrow"></div><p class="person-name">Ross Morrow</p></div>
  <a class="people-btn btn-navy abs">READ MORE</a>
</section>

<section class="contact abs" role="img" aria-label="Dimmed photo of business people in a meeting">
  <h2 class="section-title abs">Contact us</h2>
  <div class="field f-name abs">Name:</div>
  <div class="field f-phone abs">Phone:</div>
  <div class="field f-mail abs">E-Mail:</div>
  <div class="field f-msg abs">Message:</div>
  <div class="submit abs">SUBMIT</div>
</section>

<footer class="site-footer abs">
  <h2 class="footer-title abs">Get in touch with us</h2>

  <div class="office abs" style="left:78px">
    <div class="office-head"><svg width="18" height="24" viewBox="0 0 18 24"><path d="M9 0a9 9 0 0 0-9 9c0 7 9 15 9 15s9-8 9-15a9 9 0 0 0-9-9zm0 13a4 4 0 1 1 0-8 4 4 0 0 1 0 8z" fill="#2b2f36"/></svg>
      <div><p class="office-name">BELLBROOK</p><p>Suite 14, Mercer's Arcade</p><p>Bellbrook, NSW 2990</p></div></div>
    <p class="office-line"><svg width="18" height="18" viewBox="0 0 18 18"><path d="M4 1l3 4-2 2c1 2 3 4 5 5l2-2 4 3-2 3C8 16 2 10 1 4z" fill="#2b2f36"/></svg>02 5550 1400</p>
    <p class="office-line"><svg width="18" height="16" viewBox="0 0 18 16"><rect x="4" y="0" width="10" height="5" fill="#2b2f36"/><rect x="0" y="5" width="18" height="7" rx="1" fill="#2b2f36"/><rect x="4" y="10" width="10" height="6" fill="#2b2f36" stroke="#fff"/></svg>02 5550 1433</p>
    <p class="office-line"><svg width="18" height="13" viewBox="0 0 18 13"><rect width="18" height="13" fill="#2b2f36"/><path d="M0 0l9 7 9-7" fill="none" stroke="#fff" stroke-width="1.5"/></svg>info@hartwelllaw.example</p>
  </div>

  <div class="office abs" style="left:365px">
    <div class="office-head"><svg width="18" height="24" viewBox="0 0 18 24"><path d="M9 0a9 9 0 0 0-9 9c0 7 9 15 9 15s9-8 9-15a9 9 0 0 0-9-9zm0 13a4 4 0 1 1 0-8 4 4 0 0 1 0 8z" fill="#2b2f36"/></svg>
      <div><p class="office-name">KINGSFORD RIDGE</p><p>342 Ridge Street</p><p>Kingsford Ridge NSW 2991</p></div></div>
    <p class="office-line"><svg width="18" height="18" viewBox="0 0 18 18"><path d="M4 1l3 4-2 2c1 2 3 4 5 5l2-2 4 3-2 3C8 16 2 10 1 4z" fill="#2b2f36"/></svg>02 5550 2222</p>
    <p class="office-line"><svg width="18" height="16" viewBox="0 0 18 16"><rect x="4" y="0" width="10" height="5" fill="#2b2f36"/><rect x="0" y="5" width="18" height="7" rx="1" fill="#2b2f36"/><rect x="4" y="10" width="10" height="6" fill="#2b2f36" stroke="#fff"/></svg>02 5550 2244</p>
    <p class="office-line"><svg width="18" height="13" viewBox="0 0 18 13"><rect width="18" height="13" fill="#2b2f36"/><path d="M0 0l9 7 9-7" fill="none" stroke="#fff" stroke-width="1.5"/></svg>info@hartwelllaw.example</p>
  </div>

  <div class="office abs" style="left:625px">
    <div class="office-head"><svg width="18" height="24" viewBox="0 0 18 24"><path d="M9 0a9 9 0 0 0-9 9c0 7 9 15 9 15s9-8 9-15a9 9 0 0 0-9-9zm0 13a4 4 0 1 1 0-8 4 4 0 0 1 0 8z" fill="#2b2f36"/></svg>
      <div><p class="office-name">TALLOW CREEK</p><p>116 Linden Street</p><p>Tallow Creek NSW 2992</p></div></div>
    <p class="office-line"><svg width="18" height="18" viewBox="0 0 18 18"><path d="M4 1l3 4-2 2c1 2 3 4 5 5l2-2 4 3-2 3C8 16 2 10 1 4z" fill="#2b2f36"/></svg>02 5550 1400</p>
    <p class="office-note">(By Appointment)</p>
    <p class="office-line"><svg width="18" height="13" viewBox="0 0 18 13"><rect width="18" height="13" fill="#2b2f36"/><path d="M0 0l9 7 9-7" fill="none" stroke="#fff" stroke-width="1.5"/></svg>info@hartwelllaw.example</p>
  </div>

  <div class="footer-brand abs"><span class="brand-dot"></span>Hartwell Law</div>
  <div class="footer-social abs"><span></span><span></span><span></span></div>
</footer>

<div class="copyright abs">© HARTWELL LAW - 2017. All Rights Reserved</div>

</body>
</html>
```